Need a business card design. I am a Self Empowerment Life Coach.

A Life Coach is - a professional relationship designed to enhance an individual's ability to focus, make effective changes, develop oneself, achieve desired goals and maximize success in life. Coaching is about getting the very best out of someone and enabling them to make decisions that will improve their life. It is a unique way to help people look at where they are now and where they would like to be, and helps bridge the gap.

Bright Path Coaching is motivational, inspiring, positive, exciting and action driven. By raising awareness and encouraging others to take responsibility for their life, coaching can help people rise to their challenge and go further than you ever thought possible.

Industry/Entity Type

Business

Other font styles liked:
• Bookman Old Style

Requirements
Must have
• Marla Thorncastle, QTV-AR
• Self Empowerment Coach
• 318.557.6021
• mt@thebloomingpathcoach.example
• The attached logo
Nice to have
• I would like to see some designs portrait and some landscape

```html
<!DOCTYPE html>
<html lang="en">
<head>
<meta charset="utf-8">
<title>Bright Path Coaching – Business Card</title>
<link rel="stylesheet" href="https://fonts.googleapis.com/css2?family=Montserrat:wght@400;600;700&display=swap">
<style>
  :root {
    --page: #e9e7e4;
    --card: #ffffff;
    --ink: #1c1c1c;
    --slate: #5d6b6b;
    --grey: #8a8a8a;
    --band-dark: #161616;
    --band-grey: #9a9a9a;
    --shadow: rgba(0,0,0,0.18);
  }
  * { box-sizing: border-box; margin: 0; padding: 0; }
  html, body { width: 1200px; height: 900px; overflow: hidden; }
  body {
    background: var(--page);
    font-family: "Montserrat", Arial, sans-serif;
    color: var(--ink);
    position: relative;
  }
  .card {
    position: absolute;
    top: 290px;
    width: 540px;
    height: 310px;
    background: var(--card);
    box-shadow: 0 8px 24px var(--shadow);
    overflow: hidden;
  }
  .card--front { left: 45px; }
  .card--back { left: 615px; }

  .front__band {
    position: absolute; left: 0; bottom: 0;
    width: 100%; height: 90px;
    background: linear-gradient(180deg, var(--band-grey) 0%, var(--band-dark) 45%, var(--band-dark) 100%);
  }

  .identity { position: absolute; left: 34px; top: 30px; }
  .identity__name { font-size: 21px; font-weight: 700; color: var(--slate); letter-spacing: 0.3px; }
  .identity__title { font-size: 12px; color: var(--ink); margin-top: 4px; }

  .contact { position: absolute; left: 34px; top: 98px; list-style: none; }
  .contact__item { display: flex; align-items: center; gap: 8px; font-size: 10.5px; margin-bottom: 6px; color: var(--ink); }
  .contact__icon { width: 11px; height: 11px; flex: none; }

  .brand { display: flex; align-items: center; gap: 8px; }
  .brand__dot { width: 26px; height: 26px; border-radius: 50%; background: var(--grey); flex: none; }
  .brand__name { font-size: 19px; font-weight: 700; color: var(--ink); text-transform: uppercase; letter-spacing: 0.5px; line-height: 1.05; }
  .card--front .brand { position: absolute; right: 30px; top: 112px; width: 190px; }
  .card--back .brand { position: absolute; left: 50%; top: 50%; transform: translate(-50%, -50%); }
  .card--back .brand__name { font-size: 24px; }

  .front__web {
    position: absolute; right: 60px; bottom: 16px;
    font-size: 10.5px; color: #ffffff; letter-spacing: 0.5px;
  }
</style>
</head>
<body>

<section class="card card--front" aria-label="Business card front">
  <div class="front__band" role="img" aria-label="Curved black and grey decorative band along the lower edge"></div>

  <div class="identity">
    <h1 class="identity__name">Marla Thorncastle</h1>
    <p class="identity__title">Self Empowerment Coach, QTV-AR</p>
  </div>

  <ul class="contact">
    <li class="contact__item">
      <svg class="contact__icon" viewBox="0 0 12 12" aria-hidden="true"><path d="M2 1 L4.5 1 L5.5 3.5 L4 4.6 Q5 7 7.4 8 L8.5 6.5 L11 7.5 L11 10 Q6 11 2.5 7 Q0.5 4 2 1 Z" fill="var(--ink)"/></svg>
      318.555.0142
    </li>
    <li class="contact__item">
      <svg class="contact__icon" viewBox="0 0 12 12" aria-hidden="true"><rect x="1.5" y="2" width="9" height="8" fill="none" stroke="var(--ink)" stroke-width="1.2"/></svg>
      318.555.0143
    </li>
    <li class="contact__item">
      <svg class="contact__icon" viewBox="0 0 12 12" aria-hidden="true"><rect x="1" y="2.5" width="10" height="7" fill="var(--ink)"/><path d="M1 2.5 L6 6.5 L11 2.5" fill="none" stroke="#fff" stroke-width="1"/></svg>
      mt@thebloomingpathcoach.example
    </li>
    <li class="contact__item">
      <svg class="contact__icon" viewBox="0 0 12 12" aria-hidden="true"><circle cx="6" cy="6" r="4.8" fill="none" stroke="var(--ink)" stroke-width="1.1"/><path d="M1.2 6 H10.8 M6 1.2 Q3 6 6 10.8 M6 1.2 Q9 6 6 10.8" fill="none" stroke="var(--ink)" stroke-width="0.9"/></svg>
      www.brightpathcoach.example
    </li>
  </ul>

  <div class="brand">
    <span class="brand__dot" aria-hidden="true"></span>
    <span class="brand__name">Bright Path Coaching</span>
  </div>

  <p class="front__web">www.brightpathcoach.example</p>
</section>

<section class="card card--back" aria-label="Business card back">
  <div class="brand">
    <span class="brand__dot" aria-hidden="true"></span>
    <span class="brand__name">Bright Path Coaching</span>
  </div>
</section>

</body>
</html>
```